KRV Boltline Manufacturer New Web Design

We need a new theme designed for metal fastener manufacturing company, KRV Boltline Group, a $60M division of Marlow Forge Holdings, Inc. We manufacture screw, pins and washers to industrial customers (non-Automotive) such as Hollis Appliance, Carl Whitby, BRN, Venmark, etc. Our current website is www.boltline-example.com. We would like to stick with the same logo/color scheme, however, I'm aiming to modernize the website's look and feel.

Here are some of our competitor's websites:
- https://www.quorvane.example/
- http://pindrovex.example/
- http://www.harlowbuiltjoinery.example/
- http://clivetandparts.example/
- http://www.dunmerebolt.example/

Target Market(s)

We primarily want to target engineers working in the following markets:
- Appliance (Hollis Appliance, Vannoria)
- Ag (Whitby, BRN)
- Recreational Vehicle (Venmark, Glade Runner)
- Outdoor Power (Brenholt, Mivo)

We secondarily want to target buyers working at the above markets as well as buyers at Fastener distributors such as Quillory, Provender Systems, Kessel Orwin.

Industry/Entity Type

Metal Forging

Number of Pages Required

1 page

Requirements
Must have
• For products: "Threaded" product as the primary focus. "Pins" product is the secondary focus, followed by all others.
• Please use same logo and color scheme as I do not plan to change.
Nice to have
• Highlight our featured proprietary products (pamphlets attached). KRV Boltline's GRI-Z, MelDowel, Boltline Helix, Blizzard.

```html
<!DOCTYPE html>
<html lang="en">
<head>
<meta charset="utf-8">
<title>KRV Boltline Group – Better Fasteners for Better Products</title>
<link href="https://fonts.googleapis.com/css2?family=Open+Sans:wght@400;600;700&display=swap" rel="stylesheet">
<style>
:root{
  --cyan:#00b1e1;
  --teal:#00c4a0;
  --black:#000;
  --charcoal:#262626;
  --dark:#1c1c1c;
  --grey-bg:#e2e2e2;
  --white:#fff;
  --text:#222;
}
*{box-sizing:border-box;margin:0;padding:0}
html,body{width:1200px;height:2985px;overflow:hidden}
body{font-family:"Open Sans",Arial,sans-serif;color:var(--text);background:var(--white);position:relative}
.abs{position:absolute}

/* header */
.topbar{left:0;top:0;width:1200px;height:88px;background:var(--cyan)}
.topbar .brand-zone{left:0;top:0;width:560px;height:88px;background:var(--white);clip-path:polygon(0 0,100% 0,92% 100%,0 100%)}
.brand{left:96px;top:20px;display:flex;align-items:center;gap:12px}
.brand .mark{width:50px;height:50px;border-radius:50%;background:var(--cyan)}
.brand .name{font-size:30px;font-weight:700;color:var(--cyan);line-height:1}
.brand .sub{left:162px;top:56px;font-size:9px;color:#555;letter-spacing:.5px}
.search{left:544px;top:34px;width:338px;height:32px;background:var(--white);display:flex}
.search span{flex:1;font-size:14px;color:#444;padding:6px 8px}
.search .btn{width:54px;background:var(--black);display:flex;align-items:center;justify-content:center}
.social-top{left:1018px;top:56px;display:flex;gap:6px}
.social-top i,.social-foot i{display:block;width:16px;height:16px;border-radius:50%;background:var(--black)}
.nav{left:100px;top:88px;width:1100px;height:40px;background:var(--black);display:flex;padding-left:180px}
.nav a{color:var(--white);text-decoration:none;font-size:15px;padding:0 17px;line-height:40px}
.nav a.active{background:var(--cyan)}

/* hero */
.hero{left:0;top:128px;width:1200px;height:475px;background:linear-gradient(135deg,#3d3d3d,#1e1e1e 55%,#4a4a4a)}
.hero-chevron{left:0;top:88px}
.hero-title{left:478px;top:259px;width:527px;height:179px;background:rgba(230,230,230,.85);display:flex;align-items:center;justify-content:center;text-align:center;font-size:40px;font-weight:700;line-height:1.4;color:#111}

/* headings */
.section-title{width:1200px;text-align:center;font-size:30px;font-weight:700}
.section-title::after{content:"";display:block;width:180px;height:4px;margin:8px auto 0;background:currentColor}

/* products */
.products{left:0;top:603px;width:1200px;height:470px;background:var(--cyan)}
.products .section-title{color:var(--white);top:50px}
.prod-card{top:145px;width:242px;height:247px;background:var(--black)}
.prod-card .icon{position:absolute;left:71px;top:30px;width:100px;height:100px;border-radius:50%;background:var(--white)}
.prod-card .label{position:absolute;left:0;bottom:0;width:100%;height:54px;background:var(--teal);padding:6px 8px;font-size:19px;font-weight:700;color:#111}
.prod-card .label::after{content:"";display:block;width:92px;height:3px;background:#111;margin-top:2px}
.arrow{width:38px;height:38px}

/* about */
.about{left:0;top:1073px;width:1200px;height:485px;background:var(--grey-bg)}
.about .section-title{top:52px;color:#111}
.about .copy{left:96px;top:144px;width:570px;font-size:14px;line-height:1.55}
.about .copy h4{font-size:14px;font-weight:700;margin:22px 0 20px}
.read-more{display:inline-block;margin-top:22px;background:var(--cyan);color:var(--white);font-size:13px;padding:2px 12px}
.about-frame{left:752px;top:185px;width:348px;height:242px;border:2px solid var(--cyan)}
.about-photo{left:688px;top:143px;width:387px;height:257px;background:linear-gradient(120deg,#0c1a24,#1f3a4e 55%,#0a0f14)}

/* quality */
.quality{left:0;top:1558px;width:1200px;height:458px;background:linear-gradient(135deg,#2e2e2e,#141414 60%,#2a2a2a)}
.quality .section-title{top:58px;color:var(--cyan)}
.quality .section-title::after{background:var(--white);width:96px}
.quality h3{left:100px;top:186px;font-size:20px;font-weight:700;color:var(--white)}
.quality p{left:100px;top:262px;width:540px;font-size:18px;line-height:1.7;color:var(--white)}
.video{left:694px;top:153px;width:399px;height:225px;background:linear-gradient(135deg,#6f7780,#3b4047 60%,#8a9096)}

/* customers */
.customers{left:0;top:2016px;width:1200px;height:392px;background:var(--white)}
.customers .section-title{top:50px;color:var(--cyan)}
.customers .section-title::after{background:#111;width:205px}
.cust{top:160px;width:260px;height:150px;display:flex;align-items:center;justify-content:center;text-align:center;font-size:28px;font-weight:700;color:#1d3c8c}

/* contact */
.contact{left:0;top:2408px;width:1200px;height:513px;background:var(--charcoal)}
.tag{height:50px;font-size:26px;font-weight:700;padding:6px 0 0 6px}
.tag.blue{left:96px;top:0;width:214px;background:var(--cyan);color:#111;clip-path:polygon(0 0,88% 0,100% 100%,0 100%)}
.tag.green{left:677px;top:0;width:260px;background:var(--teal);color:var(--white);clip-path:polygon(0 0,88% 0,100% 100%,0 100%)}
.office{width:280px;font-size:17px;line-height:1.6;color:var(--white)}
.office b{display:block;color:var(--cyan);font-size:16px}
.mail{left:96px;top:410px;display:flex;align-items:center;gap:12px;color:var(--white);font-size:17px}
.quote{left:677px;top:50px;width:423px;height:463px;background:var(--black)}
.field{position:absolute;left:48px;width:328px;height:44px;background:var(--white);font-size:19px;color:#bbb;padding:6px 10px}
.submit{position:absolute;left:48px;top:430px;width:98px;height:34px;background:var(--teal);color:var(--white);font-size:18px;font-weight:600;text-align:center;line-height:34px}

/* footer */
.footer{left:0;top:2921px;width:1200px;height:64px;background:var(--black);color:var(--white)}
.footer .copy{left:100px;top:20px;font-size:16px}
.social-foot{left:996px;top:24px;display:flex;gap:10px}
.social-foot i{background:var(--white)}
</style>
</head>
<body>

<header>
  <div class="abs topbar">
    <div class="abs brand-zone"></div>
  </div>
  <div class="abs brand">
    <span class="mark"></span>
    <span class="name">KRV Boltline group</span>
  </div>
  <div class="abs brand sub" style="left:162px;top:60px">BOLTS • PINS • WASHERS • THREADS</div>
  <div class="abs search">
    <span>Search</span>
    <div class="btn">
      <svg width="22" height="22" viewBox="0 0 22 22"><circle cx="9" cy="9" r="6.5" fill="none" stroke="#fff" stroke-width="3"/><line x1="14" y1="14" x2="20" y2="20" stroke="#fff" stroke-width="3"/></svg>
    </div>
  </div>
  <div class="abs social-top"><i></i><i></i><i></i><i></i></div>
  <nav class="abs nav">
    <a class="active">Home</a><a>Products</a><a>Capabilties</a><a>Engineering</a><a>Quality</a><a>About Us</a><a>Contact/Quote Request</a>
  </nav>
</header>

<section class="abs hero" role="img" aria-label="Close-up photograph of a pile of steel bolts, nuts and washers"></section>
<svg class="abs hero-chevron" width="490" height="515" viewBox="0 0 490 515">
  <polygon points="240,80 330,80 150,270 490,515 340,515 60,270" fill="#00c4a0" opacity=".55"/>
</svg>
<h1 class="abs hero-title">Better Fasteners for<br>Better Products</h1>

<section class="abs products">
  <h2 class="abs section-title">Our Products</h2>
  <svg class="abs arrow" style="left:35px;top:248px" viewBox="0 0 38 38"><circle cx="19" cy="19" r="19" fill="#000"/><polyline points="22,11 14,19 22,27" fill="none" stroke="#fff" stroke-width="4"/></svg>
  <div class="abs prod-card" style="left:103px">
    <svg class="icon" viewBox="0 0 100 100"><circle cx="50" cy="50" r="20" fill="#000"/><circle cx="50" cy="50" r="6" fill="#fff"/></svg>
    <div class="label">LOCK WASHERS</div>
  </div>
  <div class="abs prod-card" style="left:354px">
    <svg class="icon" viewBox="0 0 100 100"><circle cx="40" cy="28" r="6" fill="#000"/><rect x="37" y="30" width="6" height="44" fill="#000"/><rect x="55" y="22" width="10" height="8" fill="#000"/><rect x="57" y="30" width="6" height="44" fill="#000"/></svg>
    <div class="label">PINS</div>
  </div>
  <div class="abs prod-card" style="left:607px">
    <svg class="icon" viewBox="0 0 100 100"><circle cx="50" cy="50" r="26" fill="none" stroke="#000" stroke-width="6" stroke-dasharray="8 4"/><circle cx="50" cy="50" r="16" fill="none" stroke="#000" stroke-width="5"/><circle cx="50" cy="50" r="6" fill="#000"/></svg>
    <div class="label">STAMPINGS</div>
  </div>
  <div class="abs prod-card" style="left:860px">
    <svg class="icon" viewBox="0 0 100 100"><rect x="32" y="24" width="36" height="8" fill="#000"/><rect x="32" y="35" width="36" height="8" fill="#000"/><rect x="30" y="48" width="40" height="14" fill="#000"/><rect x="40" y="62" width="20" height="14" fill="#000"/></svg>
    <div class="label">THREADED</div>
  </div>
  <svg class="abs arrow" style="left:1123px;top:248px" viewBox="0 0 38 38"><circle cx="19" cy="19" r="19" fill="#000"/><polyline points="16,11 24,19 16,27" fill="none" stroke="#fff" stroke-width="4"/></svg>
</section>

<section class="abs about">
  <h2 class="abs section-title">About Us</h2>
  <div class="abs copy">
    <p>KRV Boltline Group is a leading designer and manufacturer of value added, high quality engineered hardware solutions.</p>
    <h4>Our History</h4>
    <p>Known as KRV Boltline Group today, the company is the result of a 2010 merger of KRV businesses that have a long, rich history in the industrial hardware market. This history dates back to the 1920s, when two of KRV Boltline Group's main product lines were created.</p>
    <span class="read-more">Read More</span>
  </div>
  <div class="abs about-frame"></div>
  <div class="abs about-photo" role="img" aria-label="Photograph of an engineer working at a server rack console"></div>
</section>

<section class="abs quality">
  <h2 class="abs section-title">Quality</h2>
  <h3 class="abs">KRV Boltline Group Quality</h3>
  <p class="abs">KRV Boltline Group's quality mission is simple: To provide the highest quality, most cost effective fasteners and components.</p>
  <div class="abs video" role="img" aria-label="Embedded video still of a spring washer with a test chart"></div>
</section>

<section class="abs customers">
  <h2 class="abs section-title">Our Customers</h2>
  <svg class="abs arrow" style="left:30px;top:224px;width:32px;height:32px" viewBox="0 0 38 38"><circle cx="19" cy="19" r="19" fill="#000"/><polyline points="22,11 14,19 22,27" fill="none" stroke="#fff" stroke-width="4"/></svg>
  <div class="abs cust" style="left:96px">HOLLIS APPLIANCE</div>
  <div class="abs cust" style="left:370px;color:#2b7a2b">CARL WHITBY</div>
  <div class="abs cust" style="left:640px;color:#111;font-size:44px">BRN</div>
  <div class="abs cust" style="left:900px">VENMARK</div>
  <svg class="abs arrow" style="left:1133px;top:224px;width:32px;height:32px" viewBox="0 0 38 38"><circle cx="19" cy="19" r="19" fill="#000"/><polyline points="16,11 24,19 16,27" fill="none" stroke="#fff" stroke-width="4"/></svg>
</section>

<section class="abs contact">
  <div class="abs tag blue">Contact Us</div>
  <div class="abs office" style="left:96px;top:104px"><b>Stampings</b>1180 W Harlan Avenue<br>Fernwood, IL 60412<br>555-014-2290</div>
  <div class="abs office" style="left:404px;top:104px"><b>Lock Washers</b>4410 N Ostrand Rd<br>Dellmont, WI 53290<br>555-014-2290</div>
  <div class="abs office" style="left:96px;top:256px"><b>Pins</b>700 Foundry Rd<br>Ashcombe, WI 53077<br>555-014-2290</div>
  <div class="abs office" style="left:404px;top:256px"><b>Threaded</b>W5120 Tarn Rd<br>Millbrook, WI 53081<br>555-014-2290</div>
  <div class="abs mail">
    <svg width="38" height="28" viewBox="0 0 38 28"><rect x="1" y="1" width="36" height="26" fill="none" stroke="#00b1e1" stroke-width="2"/><polyline points="1,1 19,16 37,1" fill="none" stroke="#00b1e1" stroke-width="2"/></svg>
    sales@boltlinegroup.example
  </div>
  <div class="abs tag green">Quote Request</div>
  <form class="abs quote">
    <div class="field" style="top:42px">Name</div>
    <div class="field" style="top:118px">Email</div>
    <div class="field" style="top:194px">Mobile</div>
    <div class="field" style="top:270px;height:130px">Message</div>
    <div class="submit">Submit</div>
  </form>
</section>

<footer class="abs footer">
  <div class="abs copy">Copyright2017@KRVBoltline</div>
  <div class="abs social-foot"><i></i><i></i><i></i><i></i></div>
</footer>

</body>
</html>
```